Reputable business cards for Diplom Kauffrau, Privat und Geschäftslich

The business cards should be reputable, valuable and elegant in order to be able to use them for business. The design should also include a sophistication that is conspicuous. This could be a picture, an ornament, a sublime print or a kind of logo of the initials of my name "MK". The font should be clear and legible.
Target Market(s)
Business contacts, friends and acquaintances
Contact Information for Business Card
Diplom-Kauffrau Marietta Kuhnle
Lindenhofweg 37 50391 Kornfelde
Mobil +49 170 418 29 57
e-mail marietta.kuhnle@postfeld.de
Font styles to use
Colors
Designer to choose colors to be used in the design.
Requirements
Must have
- Clear and easy to read font My name in larger font than the other information Visual conspicuity / specificity
Nice to have
- Different colors
Should not have
- Ornate font, playful

```html
<!DOCTYPE html>
<html lang="de">
<head>
<meta charset="utf-8">
<title>Marietta Kuhnle – Visitenkarten</title>
<link rel="stylesheet" href="https://fonts.googleapis.com/css2?family=Quicksand:wght@300;400&family=Source+Sans+3:wght@400&display=swap">
<style>
  :root {
    --bg: #2b2e33;
    --card: #0b0b0c;
    --card-edge: #161618;
    --gold: #a88a5c;
    --ink: #e6e4df;
    --ink-soft: #cfcac2;
  }
  * { box-sizing: border-box; margin: 0; padding: 0; }
  html, body { width: 1200px; height: 900px; overflow: hidden; }
  body {
    background: var(--bg);
    display: flex;
    align-items: center;
    justify-content: center;
    gap: 50px;
  }
  .card {
    position: relative;
    width: 540px;
    height: 310px;
    border-radius: 26px;
    background: linear-gradient(160deg, var(--card-edge) 0%, var(--card) 60%);
    box-shadow: 0 14px 30px rgba(0,0,0,.45);
  }

  /* Front side */
  .card--front {
    display: flex;
    flex-direction: column;
    align-items: center;
    justify-content: center;
  }
  .monogram {
    width: 86px;
    height: 86px;
    border: 1.5px solid var(--gold);
    border-radius: 50%;
    display: flex;
    align-items: center;
    justify-content: center;
    font-family: "Quicksand", sans-serif;
    font-weight: 400;
    font-size: 28px;
    color: var(--ink);
    letter-spacing: 1px;
    margin-bottom: 18px;
  }
  .name {
    font-family: "Quicksand", sans-serif;
    font-weight: 300;
    color: var(--ink);
    letter-spacing: 1px;
  }
  .card--front .name { font-size: 40px; }
  .title {
    font-family: "Quicksand", sans-serif;
    font-weight: 400;
    color: var(--gold);
    text-transform: uppercase;
  }
  .card--front .title { font-size: 15px; letter-spacing: 7px; margin-top: 4px; }

  /* Back side */
  .card--back .identity { position: absolute; left: 56px; top: 50px; }
  .card--back .name { font-size: 30px; }
  .card--back .title { font-size: 11px; letter-spacing: 5.5px; margin-top: 2px; }

  .contact {
    position: absolute;
    left: 210px;
    top: 176px;
    display: flex;
    gap: 10px;
  }
  .contact__icons {
    display: flex;
    flex-direction: column;
    gap: 7px;
    padding-top: 3px;
  }
  .contact__icons svg { width: 16px; height: 16px; display: block; }
  .contact__rule { width: 1.5px; background: var(--gold); }
  .contact__lines {
    list-style: none;
    font-family: "Source Sans 3", sans-serif;
    font-size: 17px;
    line-height: 23px;
    color: var(--ink-soft);
    white-space: nowrap;
  }
</style>
</head>
<body>
  <section class="card card--back">
    <div class="identity">
      <h1 class="name">Marietta Kuhnle</h1>
      <p class="title">Diplom-Kauffrau</p>
    </div>
    <div class="contact">
      <div class="contact__icons">
        <svg viewBox="0 0 16 16" aria-label="Adresse"><path d="M8 1.5a4.5 4.5 0 0 0-4.5 4.5c0 3.2 4.5 8.5 4.5 8.5s4.5-5.3 4.5-8.5A4.5 4.5 0 0 0 8 1.5z" fill="none" stroke="#a88a5c" stroke-width="1.4"/><circle cx="8" cy="6" r="1.6" fill="#a88a5c"/></svg>
        <svg viewBox="0 0 16 16" aria-label="Mobil"><rect x="4.5" y="1.5" width="7" height="13" rx="1.4" fill="none" stroke="#a88a5c" stroke-width="1.4"/><circle cx="8" cy="12" r=".9" fill="#a88a5c"/></svg>
        <svg viewBox="0 0 16 16" aria-label="E-Mail"><rect x="1.5" y="3.5" width="13" height="9" rx="1" fill="#a88a5c"/><path d="M1.8 4l6.2 5 6.2-5" fill="none" stroke="#0b0b0c" stroke-width="1.2"/></svg>
      </div>
      <div class="contact__rule"></div>
      <ul class="contact__lines">
        <li>Lindenhofweg 37 50391 Kornfelde</li>
        <li>+49 170 418 29 57</li>
        <li>marietta.kuhnle@postfeld.de</li>
      </ul>
    </div>
  </section>

  <section class="card card--front">
    <div class="monogram">MK</div>
    <h2 class="name">Marietta Kuhnle</h2>
    <p class="title">Diplom-Kauffrau</p>
  </section>
</body>
</html>
```